Commercial New Construction and Remodeling

Residential New Construction and Remodeling

Target Market(s)

Commercial and residential, Investors

I would like you to know that I'm planning to use transparent (clear) business cards. The Logo could have colors like gray, white, lemon green.
Or another combination could be gray, white and some color between mustard or sand.

Requirements
Must have
• The Logo could be letters like HBP. I don't have preference where the Logo is on the card. And somewhere on the card the full name appears.

NAME OF THE COMPANY: HARBOR BUILDING PARTNERS
Nice to have
• I like the minimalist look,Geometric figures.

```html
<!DOCTYPE html>
<html lang="en">
<head>
<meta charset="utf-8">
<title>Harbor Building Partners — Business Card</title>
<link href="https://fonts.googleapis.com/css2?family=Montserrat:wght@400;500;600;700&display=swap" rel="stylesheet">
<style>
  :root {
    --page-bg: #e8e5e0;
    --card-dark: #121212;
    --card-clear-top: #e4e2dd;
    --card-clear-bottom: #c9c6c0;
    --lime: #c6d31f;
    --lime-deep: #a9b516;
    --swoosh-grey: #5a5650;
    --title-tone: #d9d2c6;
    --body-tone: #dcd6cc;
    --mark-tone: #2b2a28;
  }
  * { box-sizing: border-box; margin: 0; padding: 0; }
  html, body {
    width: 1200px; height: 970px; overflow: hidden;
    background: var(--page-bg);
    font-family: "Montserrat", sans-serif;
  }
  .card {
    position: absolute; left: 80px; top: 188px;
    width: 1040px; height: 594px;
    border-radius: 28px; overflow: hidden;
    background: linear-gradient(160deg, var(--card-clear-top), var(--card-clear-bottom));
    box-shadow: 0 10px 30px rgba(0,0,0,0.18);
  }
  .card-shapes { position: absolute; inset: 0; }
  .company { position: absolute; left: 42px; top: 62px; width: 470px; }
  .company-name {
    color: var(--title-tone); font-weight: 600; font-size: 33px;
    letter-spacing: 0.3px; white-space: nowrap; line-height: 1;
  }
  .company-sub {
    display: flex; align-items: center; gap: 12px; margin-top: 12px;
    color: var(--lime); font-weight: 400; font-size: 22px; letter-spacing: 7px;
  }
  .company-sub .rule { flex: 1; height: 1.5px; background: var(--lime); }
  .person-name {
    position: absolute; left: 40px; top: 236px;
    color: var(--lime); font-weight: 700; font-size: 40px; letter-spacing: 0.5px;
  }
  .address {
    position: absolute; left: 40px; top: 330px;
    color: var(--body-tone); font-size: 23px; line-height: 37px; font-weight: 400;
  }
  .contacts { position: absolute; left: 40px; top: 436px; list-style: none; }
  .contacts li {
    display: flex; align-items: center; gap: 10px; height: 37px;
    color: var(--body-tone); font-size: 23px;
  }
  .contacts svg { width: 22px; height: 22px; flex: none; }
  .brand-mark {
    position: absolute; left: 690px; top: 240px; width: 240px; text-align: center;
    color: var(--mark-tone); font-weight: 700; font-size: 104px; line-height: 1; letter-spacing: 2px;
  }
</style>
</head>
<body>
  <div class="card">
    <svg class="card-shapes" viewBox="0 0 1040 594" width="1040" height="594" aria-hidden="true">
      <path d="M0 0 H760 C560 110 540 430 720 594 H0 Z" fill="var(--card-dark)"/>
      <path d="M760 0 C560 110 540 430 720 594 H742 C585 440 592 130 800 0 Z" fill="var(--lime)"/>
      <path d="M742 594 C592 440 600 130 800 0 H806 C610 135 606 440 752 594 Z" fill="var(--lime-deep)" opacity="0.6"/>
      <path d="M600 120 C520 240 520 420 640 560 C560 430 560 250 600 120 Z" fill="var(--swoosh-grey)" opacity="0.55"/>
    </svg>

    <div class="company">
      <div class="company-name">HARBOR BUILDING</div>
      <div class="company-sub"><span class="rule"></span><span>PARTNERS</span><span class="rule"></span></div>
    </div>

    <div class="person-name">DANIEL WESTBROOK</div>

    <p class="address">Street Name Ave, Suite 100<br>State, Zip code, Country</p>

    <ul class="contacts">
      <li>
        <svg viewBox="0 0 24 24"><rect x="6" y="2" width="12" height="20" rx="2.5" fill="none" stroke="var(--lime)" stroke-width="2"/><line x1="10" y1="18.5" x2="14" y2="18.5" stroke="var(--lime)" stroke-width="2"/></svg>
        555-204-7719
      </li>
      <li>
        <svg viewBox="0 0 24 24"><rect x="2" y="5" width="20" height="14" fill="var(--lime)"/><path d="M2 5 L12 13 L22 5" fill="none" stroke="var(--card-dark)" stroke-width="1.6"/></svg>
        info@harborbuildingpartners.com
      </li>
      <li>
        <svg viewBox="0 0 24 24"><circle cx="12" cy="12" r="10" fill="var(--lime)"/><path d="M2 12 H22 M12 2 C7 7 7 17 12 22 M12 2 C17 7 17 17 12 22" fill="none" stroke="var(--card-dark)" stroke-width="1.4"/></svg>
        harborbuildingpartners.com
      </li>
    </ul>

    <div class="brand-mark">HBP</div>
  </div>
</body>
</html>
```